Book Cover,

Our book is called "88 reasons nobody warns you about adulthood: Thriving Beyond Campus, Just one more Predictable Graduate Coping Manual.
The Cover art for our book is very vivid in our minds and we hope YOU can help us bring it to life!

Picture a college graduation, cap, gown, cameras stadium the whole nine yards. now focus on one college graduate a guy, long black hair, diploma in his had, facing the crowd, his parents, flashes going off around him, behind him, is the exit of the graduation ceremony, where his class mates are exiting, but its not an exit, its the edge of a massive cliff, and students are falling down, you see people mid air falling down, at the bottom of the cliff is a trampoline, where the kids are bouncing off,

the idea and theory behind the art is the moral of the book, the book is a satire on all post college survival guides, (and god only knows how many horrible ones are out there). This is to make fun of them shed some light on the situation and really give good clear advice. so the art needs to be fun cartoonish feel and really scream satire.

Please dont hesitate to ask us for more direction, but we hope this is a great start!
Updates

Reason: We have not found something that we are set on please send us more submissions!

Reason: We have seen things we like but arent sold on any one yet- as well we have both been out of the country and have not had time to seriously consider all the submissions thank you

Target Market(s)

17-25

Industry/Entity Type

College

Requirements
Must have
• lots of colors, we want the art to be very vibrant, also a pencil look, we want the art to look like it was drawn onto the book
Should not have
• should not look digital it needs to have a real art feel to it.

```html
<!DOCTYPE html>
<html lang="en">
<head>
<meta charset="utf-8">
<title>88 Reasons Nobody Warns You About Adulthood – Book Cover</title>
<link rel="stylesheet" href="https://fonts.googleapis.com/css2?family=Teko:wght@500;600&family=Roboto+Condensed:wght@700&display=swap">
<style>
  :root {
    --backdrop: #999999;
    --paper: #ffffff;
    --band-orange: #f9a133;
    --band-red: #e8353b;
    --band-black: #000000;
    --ink: #111111;
    --author-ink: #333333;
    --rule: #cccccc;
    --pencil-light: #f4b24a;
    --pencil-dark: #c98324;
  }
  * { margin: 0; padding: 0; box-sizing: border-box; }
  html, body {
    width: 1200px;
    height: 1000px;
    overflow: hidden;
    background: var(--backdrop);
  }
  .canvas {
    position: relative;
    width: 1200px;
    height: 1000px;
    background: var(--backdrop);
  }
  .book-cover {
    position: absolute;
    left: 353px;
    top: 105px;
    width: 494px;
    height: 790px;
    background: var(--paper);
  }
  .title-block {
    position: absolute;
    left: 0;
    top: 0;
    display: block;
  }
  .title-block text {
    font-family: 'Teko', sans-serif;
    font-weight: 600;
    fill: var(--paper);
  }
  .cover-art {
    position: absolute;
    left: 117px;
    top: 455px;
    width: 232px;
    height: 55px;
    background: linear-gradient(170deg, var(--pencil-light) 0%, var(--pencil-dark) 60%, #555 100%);
    opacity: 0.55;
    border-radius: 4px;
  }
  .subtitle {
    position: absolute;
    left: 92px;
    top: 578px;
    width: 310px;
    font-family: 'Teko', sans-serif;
    font-weight: 500;
    font-size: 31px;
    line-height: 40px;
    color: var(--ink);
    text-transform: uppercase;
  }
  .subtitle span {
    display: block;
    text-align: justify;
    text-align-last: justify;
  }
  .divider {
    position: absolute;
    left: 43px;
    top: 719px;
    width: 408px;
    height: 3px;
    background: var(--rule);
  }
  .author {
    position: absolute;
    left: 0;
    top: 740px;
    width: 100%;
    text-align: center;
    font-family: 'Roboto Condensed', sans-serif;
    font-weight: 700;
    font-size: 29px;
    letter-spacing: 4px;
    color: var(--author-ink);
    text-transform: uppercase;
  }
</style>
</head>
<body>
<div class="canvas">
  <article class="book-cover">
    <svg class="title-block" width="494" height="331" viewBox="0 0 494 331" role="heading" aria-level="1" aria-label="88 Reasons Nobody Warns You About Adulthood">
      <rect class="band-orange" x="0" y="0" width="494" height="148" fill="var(--band-orange)"/>
      <rect class="band-red" x="0" y="148" width="494" height="85" fill="var(--band-red)"/>
      <rect class="band-black" x="0" y="233" width="494" height="98" fill="var(--band-black)"/>
      <text x="27" y="139" font-size="180" textLength="440" lengthAdjust="spacingAndGlyphs">88 REASONS</text>
      <text x="22" y="227" font-size="98" textLength="450" lengthAdjust="spacingAndGlyphs">NOBODY WARNS YOU</text>
      <text x="28" y="323" font-size="112" textLength="439" lengthAdjust="spacingAndGlyphs">ABOUT ADULTHOOD</text>
    </svg>

    <div class="cover-art" role="img" aria-label="Illustration of a pencil snapped in two"></div>

    <p class="subtitle">
      <span>Thriving Beyond Campus,</span>
      <span>Just one more Predictable</span>
      <span>Graduate Coping Manual</span>
    </p>

    <div class="divider"></div>

    <p class="author">Author Name</p>
  </article>
</div>
</body>
</html>
```